Horseriders ecommerce

I need the design of a web site and ecommerce for horse riders product. the actual site is brenvatoro.it and is completely to rebuild.
the most important thing that must come out from the design is that this shop sells products for both type of riding: english and western and as well has products available and good for both. (accessories and horse care)
the site owners loves much more the western riding and they want to gain a good part of customers of it, that's why i ask you to give the central area and importance to the western products.
at http://www.plokimart.com you can see a site style that we like, especially for the inner pages of products.
colors and graphics elements must be related to the world of horse riding, but we want the design to keep elegance and style, without being so western!
you need to find a way to create a cool design, user friendly to buy and that gives the real impression of professionality and care.
please check this site: http://www.quintelbazar.it/
the style is not so nice in my opinion, but somehow the navigation is friendly
in attachment to the project I add the mockup of the home page. Abou the inner page, please feel free to create the correct layout and check the one of www.plokimart.com which I like especially for the product sheet.

p.s. you can change the color of the logo
Updates

Hello dear designers,
i've pushed a little the deadline.
I will give you feedback in a while.
thaks to all
Gisetta

Target Market(s)

horse riders
western riders
english riders
stables owners

Industry/Entity Type

Product

Requirements
Must have
• style, elegance and western atmosphere. GOOD SPACES to show products.
• MUST HAVE a base way to manage banners in home page
Nice to have
• images of horses, but the most important images are products
Should not have
• too many western elements

```html
<!DOCTYPE html>
<html lang="it">
<head>
<meta charset="utf-8">
<title>Brenvatoro – Selleria</title>
<link rel="stylesheet" href="https://fonts.googleapis.com/css2?family=Oswald:wght@300;400;500&family=League+Gothic&family=Tinos&family=Arimo:wght@400;700&display=swap">
<style>
:root{
  --navy:#14213d;
  --navy-deep:#0f1a33;
  --blue:#1a5cb8;
  --blue-head:#1552a8;
  --blue-item:#3a7fd0;
  --blue-accent:#2d83d6;
  --brown:#7b3f2c;
  --brown-head:#6b3423;
  --brown-item:#8c4d38;
  --tan:#c7b692;
  --tan-head:#b9a98a;
  --tan-item:#e4d9c3;
  --tan-text:#9b8a6c;
  --black:#0b0b0b;
  --paper:#eeeeee;
  --white:#ffffff;
}
*{box-sizing:border-box;margin:0;padding:0}
html,body{width:745px;height:1200px;overflow:hidden}
body{position:relative;background:var(--white);font-family:"Arimo",sans-serif;color:var(--white)}
.abs{position:absolute}
.condensed{font-family:"League Gothic","Oswald",sans-serif;font-weight:400}

/* top bar */
.topbar{left:0;top:0;width:745px;height:26px;background:var(--navy);font-size:8px;display:flex;justify-content:flex-end;align-items:center;gap:11px;padding-right:13px}
.topbar .cart{display:flex;align-items:center;gap:5px;color:#c9d4e8}

/* header */
.header{left:0;top:26px;width:745px;height:100px;background:var(--white);border-bottom:2px dashed var(--navy)}
.logo{left:12px;top:34px;display:flex;align-items:center;gap:7px}
.logo .dot{width:30px;height:30px;border-radius:50%;background:var(--blue-head)}
.logo .name{font-family:"Oswald",sans-serif;font-weight:500;font-size:26px;color:var(--blue-head)}
.search{left:205px;top:37px;width:304px;height:29px;background:var(--navy);display:flex}
.search span{flex:1;font-size:9px;color:#d7dceb;padding:10px 12px}
.search .btn{width:40px;background:var(--blue-accent);display:flex;align-items:center;justify-content:center}
.register{left:584px;top:20px;display:flex;gap:8px;align-items:flex-start}
.register .ico{width:32px;height:24px;background:var(--blue-head);border-radius:2px;margin-top:2px}
.register b{display:block;font-family:"League Gothic",sans-serif;font-weight:400;font-size:20px;color:var(--blue-head);line-height:20px;letter-spacing:.3px}
.register small{font-size:10px;color:var(--navy)}
.share{top:63px;height:16px;border-radius:2px;font-size:5.5px;color:#fff;display:flex;align-items:center;padding-left:18px;width:73px;white-space:nowrap}
.share.pb{left:583px;background:#3a5aa0}
.share.ch{left:664px;background:#47a8e0}

/* hero */
.hero{left:0;top:130px;width:745px;height:260px;background:linear-gradient(180deg,#5a7a3a 0%,#3d5a2a 45%,#6b4a30 70%,#8a7a55 100%)}
.hero-title{left:490px;top:150px;width:237px;height:35px;background:rgba(0,0,0,.78);font-size:27px;line-height:35px;text-align:right;padding:0 16px;white-space:nowrap;letter-spacing:.3px}
.hero-text{left:330px;top:189px;width:397px;height:34px;background:rgba(20,40,90,.85);font-size:9.5px;line-height:13px;padding:5px 12px 0 19px}

/* bands */
.band-black{left:0;top:390px;width:745px;height:125px;background:var(--black)}
.band-paper{left:0;top:515px;width:745px;height:383px;background:var(--paper)}
.band-black2{left:0;top:898px;width:745px;height:222px;background:var(--black)}
.nav{left:0;top:396px;width:745px;display:flex;justify-content:space-between;font-size:21px;letter-spacing:.3px;padding:0 27px 0 33px;white-space:nowrap}

/* columns */
.col{position:absolute}
.col-head{font-family:"Oswald",sans-serif;font-weight:300;font-size:13px;text-align:center;text-transform:uppercase;letter-spacing:-.2px;white-space:nowrap}
.col.english{left:19px;top:460px;width:235px;height:616px;background:var(--brown)}
.col.english .col-head{background:var(--brown-head);height:30px;line-height:30px;color:#f2d9c6}
.col.western{left:254px;top:428px;width:236px;height:676px;background:var(--blue)}
.col.western .col-head{background:var(--blue-head);height:32px;line-height:32px}
.col.care{left:490px;top:460px;width:236px;height:616px;background:var(--tan)}
.col.care .col-head{background:var(--tan-head);height:30px;line-height:30px}
.menu{list-style:none;position:absolute;left:15px;width:208px}
.menu li{height:26px;margin-bottom:4.4px;font-family:"Tinos",serif;font-size:10.5px;line-height:26px;padding-left:11px;text-transform:uppercase;border-bottom:2px dotted rgba(255,255,255,.35);white-space:nowrap;overflow:hidden}
.english .menu{top:44px}
.english .menu li{background:var(--brown-item);color:#f4e6dc}
.western .menu{top:46px;left:14px}
.western .menu li{background:var(--blue-item)}
.care .menu{top:44px;left:14px}
.care .menu li{background:var(--tan-item);color:var(--tan-text)}

.brands{left:15px;top:418px;width:208px;height:183px;background:var(--brown-head);display:grid;grid-template-columns:1fr 1fr;gap:4px;padding:7px 5px}
.brands div{background:#efe0d6;display:flex;align-items:center;justify-content:center;font-family:"Tinos",serif;font-size:12px;color:#8a2a1e}

.saddle{left:14px;top:419px;width:210px;height:119px;background:var(--blue-head);padding:6px}
.saddle .art{width:100%;height:100%;background:linear-gradient(135deg,#4e8fd8 0%,#3a78c6 55%,#7a4a30 85%);position:relative;border:1px solid #9cc3ee}
.saddle .t1{position:absolute;left:18px;top:14px;font-family:"Oswald",sans-serif;font-weight:500;font-size:17px;line-height:19px;color:var(--navy-deep)}
.saddle .t2{position:absolute;right:12px;bottom:12px;font-family:"League Gothic",sans-serif;font-size:29px;letter-spacing:.5px;white-space:nowrap}
.gift{left:14px;top:547px;width:210px;height:119px;background:var(--blue-head);padding:6px}
.gift .card{width:100%;height:100%;background:#e0e6f0;position:relative}
.gift .gt{position:absolute;left:13px;top:18px;font-family:"Tinos",serif;font-size:34px;color:var(--blue-head);letter-spacing:-.5px;white-space:nowrap}
.gift .strip{position:absolute;left:16px;top:72px;width:166px;height:28px;background:var(--blue-head);font-size:9px;padding:10px 0 0 38px;white-space:nowrap}
.gift .buy{position:absolute;left:3px;top:65px;width:44px;height:44px;border-radius:50%;background:#4a92de;font-size:12px;text-align:center;line-height:44px}

.news{left:14px;width:208px;height:58px;background:#9b8a6c;padding:3px}
.news .in{background:#f3ecdf;width:100%;height:100%;display:flex;gap:6px;padding:4px 6px}
.news .date{width:30px;flex:none;text-align:center;font-family:"League Gothic",sans-serif;color:#8a7550}
.news .date b{display:block;width:24px;height:22px;margin:2px auto 2px;background:#9b8a6c;color:#fff;font-weight:400;font-size:16px;line-height:22px}
.news .date span{font-size:11px}
.news h4{font-family:"League Gothic",sans-serif;font-weight:400;font-size:17px;line-height:17px;color:#8a7550;text-transform:uppercase;letter-spacing:.2px}
.news p{font-size:7.5px;color:#8a7550;margin-top:2px}
.stables{left:14px;top:556px;width:208px;height:48px;background:#9b8a6c;padding:3px}
.stables .art{width:100%;height:100%;background:linear-gradient(90deg,#6b5a40,#a8957a 40%,#4a3a2a);position:relative}
.stables .art span{position:absolute;right:8px;top:9px;background:rgba(90,75,55,.8);font-family:"League Gothic",sans-serif;font-size:14px;padding:3px 8px;white-space:nowrap;letter-spacing:.3px}

/* footer */
.footer{left:0;top:1120px;width:745px;height:80px;background:var(--navy);text-align:center;font-size:8px;padding-top:15px;color:#dfe4ef}
.cards{display:flex;justify-content:center;gap:3px;margin-top:10px}
.cards span{width:44px;height:28px;background:#fff;color:var(--navy);font-size:9px;font-weight:700;line-height:28px}
</style>
</head>
<body>

<div class="abs topbar">
  <span>Contact Us</span><span>My Account</span><span>Login</span>
  <span class="cart">
    <svg width="14" height="11" viewBox="0 0 14 11"><path d="M0 1h2l2 6h7l2-5H3" fill="none" stroke="#c9d4e8" stroke-width="1.2"/><circle cx="5" cy="9.5" r="1" fill="#c9d4e8"/><circle cx="10" cy="9.5" r="1" fill="#c9d4e8"/></svg>
    Cart &nbsp; $0.00 &nbsp; 0 Items
  </span>
</div>

<header class="abs header">
  <div class="abs logo"><span class="dot"></span><span class="name">Brenvatoro</span></div>
  <div class="abs search"><span>Search Product ...</span>
    <div class="btn"><svg width="14" height="14" viewBox="0 0 14 14"><circle cx="5.5" cy="5.5" r="4.3" fill="none" stroke="#fff" stroke-width="1.6"/><path d="M8.6 8.6l4 4" stroke="#fff" stroke-width="1.8"/></svg></div>
  </div>
  <div class="abs register"><span class="ico"></span><div><b>REGISTER NOW!</b><small>get a Bday Discount</small></div></div>
  <div class="abs share pb">Share on Pagebook</div>
  <div class="abs share ch">Share on Chirper</div>
</header>

<div class="abs hero" role="img" aria-label="Three leather saddles resting on a wooden fence in front of green trees"></div>
<div class="abs hero-title condensed">SADDLES SPECIAL PROMOS</div>
<div class="abs hero-text">Lorem ipsum dolor sit amet, consectetur adipisicing elit, sed do eiusmod tempor incididunt ut labore et dolore magna aliqua. Ut enim ad minim veniam,</div>

<div class="abs band-black"></div>
<div class="abs band-paper"></div>
<div class="abs band-black2"></div>

<nav class="abs nav condensed"><span>WHO WE ARE</span><span>HOW TO BUY</span><span>SPECIAL OFFERS</span><span>PAYMENTS</span><span>BLOGSELLAVERA.IT</span></nav>

<section class="col english">
  <h2 class="col-head">English Riders &amp; Horses</h2>
  <ul class="menu">
    <li>Riservato ai maneggi</li><li>Abbigliamento</li><li>Selle e accessori</li><li>Sottopancia</li>
    <li>Riservato ai maneggi</li><li>Abbigliamento</li><li>Selle e accessori</li><li>Sottopancia</li>
    <li>Riservato ai maneggi</li><li>Abbigliamento</li><li>Selle e accessori</li><li>Sottopancia</li>
  </ul>
  <div class="abs brands">
    <div>Ferrow Hat Co.</div><div>Dalvin</div>
    <div>Trailmark</div><div>Saguel Ropes</div>
    <div>Corvano</div><div>Rangold</div>
  </div>
</section>

<section class="col western">
  <h2 class="col-head">Western Riders &amp; Horses</h2>
  <ul class="menu">
    <li>Sottopancia</li><li>Sottosella e accessori</li><li>Morsi e filetti</li><li>Equipaggiamento del cava</li>
    <li>Protezioni per cavallo</li><li>Sottosella e accessori</li><li>Morsi e filetti</li><li>Equipaggiamento del cava</li>
    <li>Protezioni per cavallo</li><li>Sottosella e accessori</li><li>Morsi e filetti</li><li>Equipaggiamento del cava</li>
  </ul>
  <div class="abs saddle">
    <div class="art" role="img" aria-label="Western saddle in brown leather on a blue background">
      <span class="t1">BUILD YOUR<br>OWN SADDLE</span><span class="t2">CLICK HERE</span>
    </div>
  </div>
  <div class="abs gift">
    <div class="card"><span class="gt">GIFT CARD</span><span class="strip">FOR FAMILY &amp; FRIENDS</span><span class="buy">BUY</span></div>
  </div>
</section>

<section class="col care">
  <h2 class="col-head">Accessories &amp; Horsecare</h2>
  <ul class="menu">
    <li>Equipaggiamento del cava</li><li>Cura del cavallo</li><li>Articoli per scuderia</li><li>Recinzioni elettriche</li>
    <li>Equipaggiamento del cava</li><li>Cura del cavallo</li><li>Articoli per scuderia</li><li>Recinzioni elettriche</li>
    <li>Equipaggiamento del cava</li><li>Cura del cavallo</li><li>Articoli per scuderia</li><li>Recinzioni elettriche</li>
  </ul>
  <article class="abs news" style="top:420px">
    <div class="in"><div class="date"><b>01</b><span>FEB</span></div>
      <div><h4>Lorem ipsum dolor sit amet, consectetur adi...</h4><p>read more</p></div></div>
  </article>
  <article class="abs news" style="top:480px">
    <div class="in"><div class="date"><b>31</b><span>JAN</span></div>
      <div><h4>Sed ut perspiciatis, unde omnis iste natu</h4><p>read more</p></div></div>
  </article>
  <div class="abs stables">
    <div class="art" role="img" aria-label="Horse stable stalls with a horse looking out"><span>PRODUCT STABLES</span></div>
  </div>
</section>

<footer class="abs footer">
  Copyright ©2012 La Selleria di Dario Fenzoli – tutti i diritti riservati – P.IVA 09283716450
  <div class="cards"><span>Paycirc</span><span>Vanta</span><span>Orbix</span></div>
</footer>

</body>
</html>
```